Drug Company Needs a Counter Display

********I am after a point of sale counter top display design. **********
^^^^^^^^^^^^^^^^^^^^^^^^^^^^^^^^^^^^^^^^^^^^^^^^^^

The design should somewhat match the current format of my products, be eye caching and modern. PLEASE REFERR TO THE ATTACHMENTS FOR INSPIRATION

What I had in mind for this project was;
If you can notice the counter display as shown in the picture with the products inside.
The bottom half of the product boxes have been cut off because of the front lip of the display, I was perhaps thinking that the display could have the bottom half of the box printed on it so it would give the illusion of a complete box.. This could be the same on the sides also, as it tapers up giving the illusion of a complete box.

I imagine possibly having the centre divider either black on the centre and then because the display is slightly larger than the boxes the "illusion" box on the left and right can be centered and then outlined with black lines.

The header board should have a clear catch phrase like "Drug Testing Kits"- easy to use -99% accuracy - fast results the text can be set on a contrasting background, solid colors are ok with gradients, swirls etc any graphic you think looks good.

Detection Times
*Depending on quantity
Ecstasy - 1 - 3 Days
Meth Amphetamine - 1 - 3 Days
Marijuana - 1 - 30 Days

This project is very open to creativity and designers can head in their own direction with this, I am not overly creative and my idea was only a suggestion.. I am keen to take on any eye catching yet professional design.

Thanks in advance.

Target Market(s)

Adults ages 18 - 45 in western speaking countries.

Industry/Entity Type

Drug

Requirements
Must have
• Easy to read text
Should not have
• cluttered text

```html
<!DOCTYPE html>
<html lang="en">
<head>
<meta charset="utf-8">
<title>Counter Display Dieline – Drug Testing Kits</title>
<link href="https://fonts.googleapis.com/css2?family=Oswald:wght@400;500;700&family=Roboto:wght@400&display=swap" rel="stylesheet">
<style>
  :root {
    --paper: #ffffff;
    --cut: #d8353a;
    --fold: #1fa36b;
    --ink-dark: #0a1119;
    --ink-mid: #16303a;
    --teal: #2f5c56;
    --text-light: #f4f6f6;
    --text-soft: #c9d3d3;
    --slogan-yellow: #f1ef3a;
    --powder: #dcdcdc;
  }
  html, body {
    margin: 0;
    padding: 0;
    width: 1200px;
    height: 927px;
    overflow: hidden;
    background: var(--paper);
  }
  .dieline {
    position: relative;
    width: 1200px;
    height: 927px;
  }
  .dieline-art {
    position: absolute;
    inset: 0;
  }
  .print-area {
    position: absolute;
    transform: rotate(180deg);
    color: var(--text-light);
    font-family: "Oswald", sans-serif;
  }
  /* Header board print */
  .header-print {
    left: 384px;
    top: 152px;
    width: 432px;
    height: 391px;
  }
  .headline {
    position: absolute;
    top: 152px;
    left: 0;
    width: 432px;
    margin: 0;
    text-align: center;
    font-weight: 700;
    font-size: 38px;
    letter-spacing: 1px;
    line-height: 1;
  }
  .tagline {
    position: absolute;
    top: 198px;
    left: 0;
    width: 432px;
    margin: 0;
    text-align: center;
    font-family: "Roboto", sans-serif;
    font-size: 12px;
    color: var(--text-soft);
  }
  .detection-title {
    position: absolute;
    top: 236px;
    left: 0;
    width: 432px;
    margin: 0;
    text-align: center;
    font-weight: 700;
    font-size: 17px;
  }
  .detection-title span {
    border-bottom: 2px solid var(--text-light);
    padding-bottom: 1px;
  }
  .detection-list {
    position: absolute;
    top: 286px;
    left: 48px;
    width: 344px;
    margin: 0;
    padding: 0;
    list-style: none;
    font-weight: 500;
    font-size: 14px;
    line-height: 22px;
  }
  .detection-list li {
    display: flex;
    justify-content: space-between;
  }
  .detection-note {
    position: absolute;
    top: 358px;
    left: 0;
    width: 432px;
    margin: 0;
    text-align: center;
    font-family: "Roboto", sans-serif;
    font-size: 9px;
    color: var(--text-soft);
  }
  /* Front lip print */
  .lip-print {
    left: 384px;
    top: 793px;
    width: 432px;
    height: 59px;
  }
  .slogan {
    position: absolute;
    top: 35px;
    left: 84px;
    width: 240px;
    margin: 0;
    display: flex;
    justify-content: space-between;
    font-weight: 500;
    font-size: 18px;
    line-height: 1;
    letter-spacing: 0.5px;
  }
  .slogan .accent { color: var(--slogan-yellow); }
  .slogan .plain { color: var(--text-light); }
  .sample-visual {
    position: absolute;
    top: 9px;
    height: 14px;
    border-radius: 7px;
    background: linear-gradient(180deg, #f3f3f3, #9a9a9a);
  }
  .sample-powder-large { left: 325px; width: 48px; }
  .sample-powder-small { left: 188px; width: 34px; }
  .sample-pill { left: 68px; width: 18px; background: linear-gradient(180deg, #f7f7ee, #c9c9b8); }
</style>
</head>
<body>
<main class="dieline">
  <svg class="dieline-art" width="1200" height="927" viewBox="0 0 1200 927" aria-hidden="true">
    <defs>
      <radialGradient id="header-glow" cx="0.5" cy="0.5" r="0.7">
        <stop offset="0" stop-color="#2b4f50"/>
        <stop offset="0.6" stop-color="#152a33"/>
        <stop offset="1" stop-color="#0b161f"/>
      </radialGradient>
      <linearGradient id="front-sweep" x1="0" y1="0" x2="1" y2="0">
        <stop offset="0" stop-color="#163331"/>
        <stop offset="0.1" stop-color="#2f5c56"/>
        <stop offset="0.55" stop-color="#10242b"/>
        <stop offset="1" stop-color="#070c14"/>
      </linearGradient>
      <linearGradient id="side-left" x1="0" y1="0" x2="1" y2="0">
        <stop offset="0" stop-color="#0c1820"/>
        <stop offset="0.65" stop-color="#2f5c56"/>
        <stop offset="1" stop-color="#1a3434"/>
      </linearGradient>
      <linearGradient id="side-right" x1="0" y1="0" x2="1" y2="0">
        <stop offset="0" stop-color="#0c1820"/>
        <stop offset="0.6" stop-color="#2f5c56"/>
        <stop offset="1" stop-color="#163030"/>
      </linearGradient>
      <linearGradient id="lip-band" x1="0" y1="0" x2="1" y2="0">
        <stop offset="0" stop-color="#1e3a3a"/>
        <stop offset="0.5" stop-color="#152a31"/>
        <stop offset="1" stop-color="#0c151d"/>
      </linearGradient>
    </defs>

    <g class="cut-lines" fill="none" stroke="var(--cut)" stroke-width="1">
      <!-- top dust flaps -->
      <path d="M384 152 V16 Q384 10 390 10 H598 V152"/>
      <path d="M603 152 V10 H810 Q816 10 816 16 V152"/>
      <!-- header wings -->
      <path d="M384 398 L240 452 V543"/>
      <path d="M816 398 L960 452 V543"/>
      <!-- outer side flaps -->
      <path d="M240 543 L128 635 L170 690 L166 694 L245 796 L285 826 L330 793"/>
      <path d="M960 543 L1072 635 L1030 690 L1034 694 L955 796 L915 826 L870 793"/>
      <!-- lip corner tabs -->
      <path d="M330 793 V852 H384"/>
      <path d="M870 793 V852 H816"/>
      <!-- bottom flaps -->
      <path d="M388 852 V908 Q388 914 394 914 H598 V852"/>
      <path d="M603 852 V914 H806 Q812 914 812 908 V852"/>
      <!-- tear-away insert -->
      <path d="M848 52 L975 43 L990 78 L1052 70 L1135 128 L945 400 L935 345 L928 338 L878 382 L870 340 Z"/>
    </g>

    <g class="print-panels">
      <rect x="384" y="152" width="432" height="391" fill="url(#header-glow)"/>
      <rect x="384" y="543" width="432" height="250" fill="url(#front-sweep)"/>
      <polygon points="240,543 384,543 384,793 330,793" fill="url(#side-left)"/>
      <polygon points="816,543 960,543 870,793 816,793" fill="url(#side-right)"/>
      <rect x="384" y="793" width="432" height="59" fill="url(#lip-band)"/>
    </g>

    <g class="fold-lines" fill="none" stroke="var(--fold)" stroke-width="1">
      <rect x="384" y="152" width="432" height="700"/>
      <line x1="384" y1="272" x2="816" y2="272"/>
      <line x1="384" y1="278" x2="816" y2="278"/>
      <line x1="384" y1="397" x2="816" y2="397"/>
      <line x1="240" y1="543" x2="960" y2="543"/>
      <line x1="384" y1="793" x2="816" y2="793"/>
      <line x1="330" y1="793" x2="384" y2="793"/>
      <line x1="816" y1="793" x2="870" y2="793"/>
      <line x1="598" y1="10" x2="598" y2="152"/>
      <line x1="240" y1="543" x2="330" y2="793"/>
      <line x1="960" y1="543" x2="870" y2="793"/>
      <line x1="870" y1="340" x2="928" y2="338"/>
      <line x1="853" y1="92" x2="990" y2="78"/>
      <line x1="990" y1="78" x2="928" y2="338"/>
      <line x1="997" y1="80" x2="935" y2="345"/>
      <line x1="990" y1="78" x2="1112" y2="158"/>
      <line x1="935" y1="345" x2="970" y2="366"/>
    </g>

    <g class="slot-cuts" fill="none" stroke="var(--cut)" stroke-width="1">
      <rect x="386" y="614" width="5" height="106" rx="2.5"/>
      <rect x="809" y="614" width="5" height="106" rx="2.5"/>
      <rect x="452" y="788" width="88" height="6" rx="3"/>
      <rect x="662" y="788" width="88" height="6" rx="3"/>
    </g>
  </svg>

  <section class="print-area header-print" aria-label="Header board">
    <h1 class="headline">DRUG TESTING KITS</h1>
    <p class="tagline">easy to use -99% accuracy - fast results</p>
    <h2 class="detection-title"><span>Drug Detection Times</span></h2>
    <ul class="detection-list">
      <li><span>- Ecstasy (MDMA)</span><span>2-3 days</span></li>
      <li><span>- Meth Amphetamine</span><span>2-3 days</span></li>
      <li><span>- Marijuana (THC)</span><span>1-7 Days</span></li>
    </ul>
    <p class="detection-note">*detection times may be longer when frequent use is present</p>
  </section>

  <section class="print-area lip-print" aria-label="Front lip">
    <p class="slogan">
      <span class="accent">DONT</span>
      <span class="accent">TAKE</span>
      <span class="plain">THE</span>
      <span class="plain">HIGH</span>
      <span class="accent">ROAD</span>
    </p>
    <div class="sample-visual sample-powder-large" role="img" aria-label="Line of white powder"></div>
    <div class="sample-visual sample-powder-small" role="img" aria-label="Small pile of white powder"></div>
    <div class="sample-visual sample-pill" role="img" aria-label="Pressed pill"></div>
  </section>
</main>
</body>
</html>
```